Beer Bottle Label

We are a boutique brewery. We need to design beer bottle labels. Our image theme so far has incorporated oil paintings from an Australian artist, and we would like to continue this theme. I will attach a demo label that I made (it's terrible!), and the image we would like to incorporate in the first design. I will also attach an image of the beer tap badge. We would like a label shaped like the demo I provide, or a rectangular label 8cm high * 15cm long. We are looking for a 'classy' label. The label also needs to incorporate our business logo, which I have attached. The Label must also include, in small writing: '4.5%abv' and 'contains approx. 1.2 standard drinks' and '330mL' and 'Brewed by Fenwary Ales. 48 Pellam Road, Durnside Victoria Australia 3279'.
If we receive an acceptable design from ArtHively, we would like you to design our other bottle labels, and redesign our beer tap badges.

Target Market(s)

Australian craft beer consumers

Industry/Entity Type

Boutique

Requirements
Must have
• Legal requirements: '4.5%abv' and 'contains approx. 1.2 standard drinks' and '330mL' and 'Brewed by Fenwary Ales. 48 Pellam Road, Durnside Victoria Australia 3279'
• Our business logo (see attached file).
• Must also utilise the painting (see attached file)

```html
<!DOCTYPE html>
<html lang="en">
<head>
<meta charset="utf-8">
<title>Durnside Draught – Bottle Label</title>
<link rel="stylesheet" href="https://fonts.googleapis.com/css2?family=Cinzel:wght@400;600;700&display=swap">
<style>
  :root {
    --backdrop: #e6e6e6;
    --label-white: #f7f7f5;
    --ink: #1d1d1b;
    --band: #0f0f0f;
    --band-text: #e9e9e6;
    --title-light: #fbfaf4;
    --brand-green: #3f8f6a;
    --paint-sky: #c9c4a8;
    --paint-field: #8d8450;
    --paint-earth: #5e4a30;
  }
  * { margin: 0; padding: 0; box-sizing: border-box; }
  html, body {
    width: 1200px; height: 1200px; overflow: hidden;
    background: radial-gradient(circle at 50% 40%, #fbfbfb 0%, var(--backdrop) 75%);
    font-family: "Cinzel", serif;
  }
  .label {
    position: absolute; left: 220px; top: 170px;
    width: 760px; height: 860px;
    background: var(--label-white);
    box-shadow: 0 12px 40px rgba(0,0,0,0.12);
    overflow: hidden;
  }
  .label__painting {
    position: absolute; left: 0; top: 0; width: 100%; height: 360px;
    background: linear-gradient(180deg, var(--paint-sky) 0%, #a9a47a 35%, var(--paint-field) 65%, var(--paint-earth) 100%);
  }
  .label__painting::after {
    content: ""; position: absolute; left: 0; right: 0; bottom: 0; height: 60px;
    background: linear-gradient(180deg, rgba(247,247,245,0) 0%, var(--label-white) 100%);
  }
  .label__place {
    position: absolute; left: 0; width: 100%; top: 262px;
    text-align: center; font-weight: 600; font-size: 76px; letter-spacing: 1px;
    color: var(--title-light);
    text-shadow: 0 2px 3px rgba(0,0,0,0.75), 0 0 10px rgba(0,0,0,0.4);
  }
  .label__style {
    position: absolute; left: 0; width: 100%; top: 360px;
    text-align: center; font-weight: 400; font-size: 72px; color: var(--ink);
  }
  .brand {
    position: absolute; left: 90px; top: 490px;
    display: flex; align-items: center; gap: 34px;
  }
  .brand__mark {
    width: 130px; height: 130px; border-radius: 50%;
    background: var(--brand-green); flex: none;
  }
  .brand__text { color: var(--ink); }
  .brand__name {
    display: block; font-weight: 700; font-size: 54px; line-height: 1.05;
  }
  .brand__kind {
    display: block; margin-top: 6px;
    font-weight: 600; font-size: 24px;
  }
  .brand__town {
    display: block; margin-top: 6px;
    font-weight: 400; font-size: 18px;
  }
  .label__band {
    position: absolute; left: 0; top: 690px; width: 100%; height: 120px;
    background: var(--band); color: var(--band-text);
    display: flex; align-items: center; justify-content: space-between;
    padding: 0 60px 0 110px;
  }
  .legal {
    font-size: 13px; line-height: 1.6; letter-spacing: 0.5px;
  }
  .measures { text-align: right; }
  .abv { display: block; font-size: 26px; }
  .volume { display: block; margin-top: 4px; font-size: 16px; }
</style>
</head>
<body>
  <div class="label">
    <div class="label__painting" role="img" aria-label="Oil painting of drovers with a horse-drawn cart and team of horses in the Australian bush"></div>
    <div class="label__place">DURNSIDE</div>
    <div class="label__style">DRAUGHT</div>

    <div class="brand">
      <div class="brand__mark"></div>
      <div class="brand__text">
        <span class="brand__name">YARRABEE</span>
        <span class="brand__kind">BREWERY AND DISTILLERY</span>
        <span class="brand__town">Durnside Victoria.</span>
      </div>
    </div>

    <div class="label__band">
      <div class="legal">BREWED BY FENWARY ALES.<br>48 PELLAM ROAD, DURNSIDE<br>VICTORIA AUSTRALIA 3279<br>CONTAINS APPROX. 1.2 STANDARD DRINKS</div>
      <div class="measures">
        <span class="abv">4.5%ABV</span>
        <span class="volume">330mL</span>
      </div>
    </div>
  </div>
</body>
</html>
```